Awards Banquet Invitation

The Millbrook Valley Chamber of Commerce is celebrating it's 65th year at our Annual Awards Banquet (business leader awards). Since we were founded in 1950, we will have a 1950's theme. Dress will be 1950's Formal. I don't want cheesy 1950's. I want Classic feel and fonts from that era. This event is for business professionals so looks from ads in the 50's would be good for inspiration. I would like a look that I can use for the program and event ads. Invitation will include an RSVP insert. Date: February 10, 2015. Time: 6 cocktails, 7 dinner & program, Location: Delwen Oaks Country Club. Dress is 1950's formal

Target Market(s)

Business owners - our members

Industry/Entity Type

Business

• Lasalle, linotype, thirsty

Colors
86cfc6
474747
ffffff
000000

Requirements
Must have
• classic 50's font and old-fashioned feel
Should not have
• sock hop, soda fountain, 50's diner

```html
<!DOCTYPE html>
<html lang="en">
<head>
<meta charset="utf-8">
<title>Annual Awards Banquet Invitation</title>
<link href="https://fonts.googleapis.com/css2?family=Yellowtail&family=Yanone+Kaffeesatz:wght@500;600&family=Wellfleet&family=Dancing+Script:wght@500;700&display=swap" rel="stylesheet">
<style>
  :root {
    --backdrop: #7a4f2f;
    --card: #231f20;
    --ink-white: #ffffff;
    --accent-red: #e01f26;
    --rule: #d9d9d9;
  }
  html, body {
    margin: 0;
    padding: 0;
    width: 1200px;
    height: 853px;
    overflow: hidden;
    background: var(--backdrop);
  }
  .canvas {
    position: relative;
    width: 1200px;
    height: 853px;
  }
  .card {
    position: absolute;
    background: var(--card);
    box-sizing: border-box;
    overflow: hidden;
  }
  .card__frame {
    position: absolute;
    inset: 13px;
    border: 3px solid var(--ink-white);
    border-radius: 3px;
  }
  .centered {
    position: absolute;
    left: 24px;
    right: 24px;
    text-align: center;
    color: var(--ink-white);
    white-space: nowrap;
  }
  .stars {
    position: absolute;
    left: 50%;
    transform: translateX(-50%);
  }
  .ribbon {
    position: absolute;
    left: 50%;
    transform: translateX(-50%);
  }
  .ribbon__text {
    position: absolute;
    inset: 0;
    display: flex;
    align-items: center;
    justify-content: center;
    color: var(--ink-white);
    font-family: "Yanone Kaffeesatz", sans-serif;
    font-weight: 600;
    white-space: nowrap;
  }
  .script-title {
    font-family: "Yellowtail", "Dancing Script", cursive;
    font-weight: 400;
    color: var(--accent-red);
    line-height: 1;
  }
  .retro-caption {
    font-family: "Wellfleet", serif;
  }
  .condensed {
    font-family: "Yanone Kaffeesatz", sans-serif;
    font-weight: 500;
  }
  .double-rule {
    position: absolute;
    left: 40px;
    right: 40px;
    height: 5px;
    border-top: 1px solid var(--rule);
    border-bottom: 1px solid var(--rule);
  }
  .starburst {
    position: absolute;
    width: 40px;
    height: 40px;
    border-radius: 50%;
    background: radial-gradient(circle, rgba(255,255,255,0.35), rgba(255,255,255,0.04) 70%);
  }

  /* Invitation */
  .invitation { left: 150px; top: 86px; width: 430px; height: 680px; }
  .invitation .stars--top { top: 36px; }
  .invitation .ribbon { top: 74px; width: 350px; height: 42px; }
  .invitation .ribbon__text { font-size: 20px; }
  .invitation__host { top: 132px; font-size: 14px; }
  .invitation__title-line1 { top: 170px; font-size: 60px; }
  .invitation__title-line2 { top: 238px; font-size: 58px; }
  .invitation .starburst--left { left: 52px; top: 252px; }
  .invitation .starburst--right { right: 52px; top: 252px; }
  .invitation .double-rule--upper { top: 322px; }
  .invitation__date { top: 362px; font-size: 34px; }
  .invitation__venue { top: 444px; font-size: 30px; }
  .invitation__details { top: 522px; font-size: 23px; }
  .invitation__details .dot { color: var(--accent-red); }
  .invitation .double-rule--lower { top: 586px; }
  .invitation .stars--bottom { bottom: 40px; }

  /* RSVP insert */
  .rsvp { left: 628px; top: 372px; width: 440px; height: 320px; }
  .rsvp__title { top: 28px; font-size: 80px; letter-spacing: 2px; }
  .rsvp .stars { top: 118px; }
  .rsvp__prompt { top: 138px; font-size: 13px; }
  .rsvp .ribbon { top: 160px; width: 250px; height: 48px; }
  .rsvp .ribbon__text { font-size: 28px; }
  .rsvp .starburst--left { left: 38px; top: 90px; }
  .rsvp .starburst--right { right: 34px; top: 192px; }
  .rsvp__field {
    position: absolute;
    left: 110px;
    color: var(--ink-white);
    font-size: 18px;
    display: flex;
    align-items: flex-end;
  }
  .rsvp__field-line {
    display: inline-block;
    border-bottom: 1px solid var(--ink-white);
    margin-left: 6px;
    margin-bottom: 4px;
  }
  .rsvp__field--name { top: 222px; }
  .rsvp__field--name .rsvp__field-line { width: 205px; }
  .rsvp__field--guest { top: 246px; }
  .rsvp__field--guest .rsvp__field-line { width: 180px; }
  .rsvp__choice {
    position: absolute;
    top: 278px;
    display: flex;
    align-items: center;
    gap: 8px;
    color: var(--ink-white);
    font-family: "Dancing Script", cursive;
    font-size: 11px;
    white-space: nowrap;
  }
  .rsvp__choice-dot {
    width: 20px;
    height: 20px;
    border-radius: 50%;
    background: var(--accent-red);
  }
  .rsvp__choice--accept { left: 104px; }
  .rsvp__choice--decline { left: 250px; }
</style>
</head>
<body>
<main class="canvas">

  <section class="card invitation" aria-label="Awards banquet invitation">
    <div class="card__frame"></div>

    <svg class="stars stars--top" width="96" height="22" viewBox="0 0 96 22" aria-hidden="true">
      <g fill="#ffffff">
        <polygon points="12,1 15,8 22,8 16.5,12.5 18.5,20 12,15.5 5.5,20 7.5,12.5 2,8 9,8"/>
        <polygon points="48,0 51.5,8 59,8 53,13 55,21 48,16.5 41,21 43,13 37,8 44.5,8"/>
        <polygon points="84,1 87,8 94,8 88.5,12.5 90.5,20 84,15.5 77.5,20 79.5,12.5 74,8 81,8"/>
      </g>
    </svg>

    <div class="ribbon">
      <svg width="350" height="42" viewBox="0 0 350 42" aria-hidden="true">
        <polygon points="0,6 350,0 334,21 350,42 0,42 16,24" fill="#e01f26"/>
      </svg>
      <div class="ribbon__text">Please join us as we celebrate our 65<sup style="font-size:11px">th</sup>&nbsp;anniversary</div>
    </div>

    <div class="centered retro-caption invitation__host">The Millbrook Valley Chamber of Commerce</div>

    <div class="centered script-title invitation__title-line1">Annual Awards</div>
    <div class="starburst starburst--left" role="img" aria-label="Atomic starburst ornament"></div>
    <div class="centered script-title invitation__title-line2">Banquet</div>
    <div class="starburst starburst--right" role="img" aria-label="Atomic starburst ornament"></div>

    <div class="double-rule double-rule--upper"></div>

    <div class="centered condensed invitation__date">February 10, 2015</div>
    <div class="centered condensed invitation__venue">at the Delwen Oaks Country Club</div>
    <div class="centered condensed invitation__details">50s Formal Attire <span class="dot">•</span> 6 cocktails, 7 dinner &amp; program</div>

    <div class="double-rule double-rule--lower"></div>

    <svg class="stars stars--bottom" width="96" height="22" viewBox="0 0 96 22" aria-hidden="true">
      <g fill="#ffffff">
        <polygon points="12,1 15,8 22,8 16.5,12.5 18.5,20 12,15.5 5.5,20 7.5,12.5 2,8 9,8"/>
        <polygon points="48,0 51.5,8 59,8 53,13 55,21 48,16.5 41,21 43,13 37,8 44.5,8"/>
        <polygon points="84,1 87,8 94,8 88.5,12.5 90.5,20 84,15.5 77.5,20 79.5,12.5 74,8 81,8"/>
      </g>
    </svg>
  </section>

  <section class="card rsvp" aria-label="RSVP card">
    <div class="card__frame"></div>

    <div class="centered script-title rsvp__title">RSVP</div>
    <div class="starburst starburst--left" role="img" aria-label="Atomic starburst ornament"></div>

    <svg class="stars" width="60" height="14" viewBox="0 0 96 22" aria-hidden="true">
      <g fill="#ffffff">
        <polygon points="12,1 15,8 22,8 16.5,12.5 18.5,20 12,15.5 5.5,20 7.5,12.5 2,8 9,8"/>
        <polygon points="48,0 51.5,8 59,8 53,13 55,21 48,16.5 41,21 43,13 37,8 44.5,8"/>
        <polygon points="84,1 87,8 94,8 88.5,12.5 90.5,20 84,15.5 77.5,20 79.5,12.5 74,8 81,8"/>
      </g>
    </svg>

    <div class="centered retro-caption rsvp__prompt">Please respond by</div>

    <div class="ribbon">
      <svg width="250" height="48" viewBox="0 0 250 48" aria-hidden="true">
        <polygon points="0,0 250,6 236,26 250,48 0,42 14,21" fill="#e01f26"/>
      </svg>
      <div class="ribbon__text">February 10, 2015</div>
    </div>

    <div class="starburst starburst--right" role="img" aria-label="Atomic starburst ornament"></div>

    <div class="rsvp__field rsvp__field--name condensed">M<span class="rsvp__field-line"></span></div>
    <div class="rsvp__field rsvp__field--guest condensed">Guest<span class="rsvp__field-line"></span></div>

    <div class="rsvp__choice rsvp__choice--accept"><span class="rsvp__choice-dot"></span>accepts with pleasure</div>
    <div class="rsvp__choice rsvp__choice--decline"><span class="rsvp__choice-dot"></span>declines with regrets</div>
  </section>

</main>
</body>
</html>
```